New College Graduate Resume - Creative and unique design that stands out from the rest

Need creative resume design for recent college graduate who graduated from School of Music with a concentration in music composition and production. Striving for a contemporary layout/design that allows the resume to "be unique" and "stand out" but be polished and professional. Open to integrating moderate color/graphics as part of resume design but the design can be minus those attributes as well. Attached is raw content in 7 sections (name/contact info, education, highlights of qualifications, work experience, honors/awards, and professional affiliations). While the designer has full latitude over overall design which (section headers, font type, separation/spacing, use of bullets, justification of text, etc.) please maintain current order/sequence of the 7 sections.

Industry/Entity Type

School

Requirements
Must have
• Name (Tobias Hale Whitcombe II) should be most prominent (bold/font size) compared to remainder of resume copy.
• Section headers should be prominent but less so when compared to name on resume.
• The attached file of resume content is provided as raw source copy and is NOT to be just copied and pasted into open fields as is. Expectation is each section of copy will be organized in a manner that is most visually appealing and may include bullets, appropriate spacing, etc.
Should not have
• The attached file of resume content is provided as source copy and is NOT to be just copied and pasted into open fields as is. Expectation is each section of copy will be organized in a manner that

```html
<!DOCTYPE html>
<html lang="en">
<head>
<meta charset="utf-8">
<title>Tobias Hale Whitcombe II — Resume</title>
<link rel="stylesheet" href="https://fonts.googleapis.com/css2?family=Oswald:wght@400;500&family=Questrial&display=swap">
<style>
  :root {
    --sky: #62b5e2;
    --sky-pale: #e3eff8;
    --ink: #1c1c1c;
    --ink-soft: #3a3a3a;
    --paper: #ffffff;
    --backdrop: #ececec;
    --photo-tone-a: #c9b8a8;
    --photo-tone-b: #e6e8ea;
  }
  * { box-sizing: border-box; margin: 0; padding: 0; }
  html, body { width: 1200px; height: 1200px; overflow: hidden; }
  body {
    background: var(--backdrop);
    font-family: "Questrial", "Century Gothic", sans-serif;
    color: var(--ink);
    position: relative;
  }
  .resume {
    position: absolute;
    left: 205px; top: 43px;
    width: 790px; height: 1114px;
    background: var(--paper);
    overflow: hidden;
  }
  .masthead {
    position: absolute; left: 0; top: 0; width: 100%; height: 128px;
    background: var(--sky);
  }
  .contact-band {
    position: absolute; left: 0; top: 128px; width: 100%; height: 71px;
    background: var(--sky-pale);
  }
  .name {
    position: absolute; left: 48px; top: 46px;
    font-family: "Oswald", "Arial Narrow", sans-serif;
    font-weight: 400; font-size: 47px; line-height: 1;
    color: var(--paper); letter-spacing: 0.2px; white-space: nowrap;
  }
  .tagline {
    position: absolute; left: 49px; top: 101px;
    font-family: "Oswald", "Arial Narrow", sans-serif;
    font-size: 13px; letter-spacing: 1.6px; color: var(--paper);
  }
  .contact { position: absolute; left: 48px; top: 136px; font-size: 13px; color: var(--ink-soft); }
  .contact li { list-style: none; display: flex; align-items: center; height: 19.5px; }
  .contact svg { width: 14px; height: 14px; margin-right: 9px; fill: var(--sky); }
  .contact .strong { font-weight: 700; color: var(--ink); }
  .contact .label { color: var(--sky); font-weight: 700; margin-right: 5px; }
  .portrait {
    position: absolute; left: 593px; top: 22px; width: 151px; height: 177px;
    background: var(--paper); padding: 6px 6px 0;
  }
  .portrait div {
    width: 100%; height: 100%;
    background: linear-gradient(180deg, var(--photo-tone-b) 0%, var(--photo-tone-a) 55%, var(--photo-tone-b) 100%);
  }
  .section-head {
    position: absolute; display: flex; align-items: center;
    background: var(--sky); color: var(--paper);
    font-family: "Oswald", "Arial Narrow", sans-serif; font-size: 27px; line-height: 1;
    padding-left: 12px;
  }
  .section-head svg { width: 22px; height: 22px; margin-right: 9px; stroke: var(--paper); fill: none; stroke-width: 1.6; }
  .head-profile { left: 48px; top: 259px; width: 407px; height: 35px; }
  .head-education { left: 48px; top: 473px; width: 407px; height: 35px; }
  .head-work { left: 48px; top: 715px; width: 407px; height: 35px; }
  .head-highlights { left: 503px; top: 259px; width: 242px; height: 65px; align-items: center; }
  .head-highlights span { line-height: 0.95; }
  .head-highlights svg { width: 32px; height: 36px; }
  .profile-text {
    position: absolute; left: 48px; top: 305px; width: 407px;
    font-size: 13.8px; line-height: 17.6px; text-align: justify; color: var(--ink-soft);
  }
  .education { position: absolute; left: 48px; top: 518px; width: 407px; font-size: 14px; line-height: 18px; }
  .education .entry { margin-bottom: 17px; }
  .education b { font-weight: 700; color: var(--ink); }
  .education em { font-style: italic; }
  .work { position: absolute; left: 48px; top: 766px; width: 700px; font-size: 14px; line-height: 18px; }
  .work .place { font-style: normal; }
  .work .city { font-style: italic; font-weight: 700; }
  .work ul { margin-top: 10px; list-style: none; }
  .work li { position: relative; padding-left: 22px; line-height: 20px; font-size: 13.8px; color: var(--ink-soft); }
  .work li::before, .skills li::before {
    content: ""; position: absolute; left: 2px; top: 8px;
    width: 6px; height: 6px; border-radius: 50%; background: var(--sky);
  }
  .skills { position: absolute; left: 515px; top: 337px; width: 230px; list-style: none; font-size: 13.8px; color: var(--ink-soft); }
  .skills li { position: relative; padding-left: 15px; line-height: 15.5px; margin-bottom: 7px; }
  .skills li::before { left: 0; top: 6px; width: 5px; height: 5px; }
</style>
</head>
<body>
  <main class="resume">
    <header class="masthead">
      <h1 class="name">TOBIAS HALE WHITCOMBE II</h1>
      <p class="tagline">MUSIC COMPOSITION AND PRODUCTION</p>
    </header>
    <section class="contact-band">
    </section>
    <ul class="contact">
      <li><svg viewBox="0 0 16 16"><rect x="1" y="1" width="14" height="14" rx="2"/><path d="M5 4c1 3 3 6 6 8l1.5-1.5-2-1.5-1 1c-1-.7-2-1.8-2.6-3l1-1-1.5-2z" fill="#fff"/></svg><span class="strong">404-555-0182</span></li>
      <li><svg viewBox="0 0 16 16"><rect x="1" y="3" width="14" height="10" rx="1"/><path d="M1.5 4l6.5 5 6.5-5" stroke="#fff" stroke-width="1.3" fill="none"/></svg><span class="strong">thwhitcombe@mailbox.com</span></li>
      <li><span class="label">ADD:</span>218 Larkspur Lane, Atlanta, Georgia&nbsp;&nbsp;30309</li>
    </ul>
    <figure class="portrait"><div role="img" aria-label="Portrait photograph of the candidate in a white shirt and dark tie"></div></figure>

    <h2 class="section-head head-profile"><svg viewBox="0 0 24 24"><circle cx="12" cy="8" r="4.5"/><path d="M3.5 21c0-4.5 3.8-7.5 8.5-7.5s8.5 3 8.5 7.5z"/></svg>PROFILE</h2>
    <p class="profile-text">Recent graduate of a highly ranked university seeking opportunities to apply composition and production talents across a variety of music genres and other media. Expertise lies in delivering high quality sound design, editing, mixing, and recording. Excellent interpersonal skills and the ability to build strong relationships with people at all levels. Exceptionally motivated self-starter and creative problem solver who enjoys working collaboratively on teams.</p>

    <h2 class="section-head head-education"><svg viewBox="0 0 24 24" style="fill:#fff;stroke:none"><path d="M12 4L1 9l11 5 9-4.1V16h1.6V9z"/><path d="M5.5 12.5v4c2 2.2 11 2.2 13 0v-4L12 15.5z"/></svg>EDUCATION</h2>
    <div class="education">
      <div class="entry"><b>BRIGHTWATER SCHOOL OF MUSIC</b> - Coastal Bay University<br><em>Coral Springs, Florida</em></div>
      <div class="entry"><b>BACHELOR OF MUSIC</b> | May 2016<br>Major: Media Writing and Production, <b>GPA 3.20/4.0</b></div>
      <div class="entry"><b>ASHFORD HILL ACADEMY</b> | May 2011<br>High School Diploma <b>with Honors</b><br><em>College Park, Georgia</em></div>
    </div>

    <h2 class="section-head head-work"><svg viewBox="0 0 24 24"><rect x="2.5" y="7" width="19" height="13" rx="1"/><path d="M8.5 7V4h7v3M7 7v13M17 7v13"/></svg>WORK EXPERIENCE</h2>
    <div class="work">
      <p><b>SOUND ENGINEER</b> | May 2014 – Present<br><span class="place">Sunline Film Studio (SFS), </span><span class="city">Miami, FL</span></p>
      <ul>
        <li>Edited and mixed recorded field audio to professional standards.</li>
        <li>Matched audio with motion picture video to create a seamless product.</li>
        <li>Recorded automated dialogue replacement (ADR) audio and integrated into motion picture video project using SoundDesk 11.</li>
        <li>Recorded foley sound effects to be added to film, video, and other media in post-production.</li>
        <li>Composed and recorded original music to accompany various video projects.</li>
      </ul>
    </div>

    <h2 class="section-head head-highlights"><svg viewBox="0 0 24 28"><path d="M12 2a8 8 0 0 0-5 14.2c1 .9 1.5 2 1.5 3.3h7c0-1.3.5-2.4 1.5-3.3A8 8 0 0 0 12 2z"/><path d="M8.5 22.5h7M9.5 25.5h5"/><path d="M12 6a4 4 0 0 0-4 4"/></svg><span>HIGHLIGHTS OF<br>QUALIFICATIONS</span></h2>
    <ul class="skills">
      <li>Media Production<br>Software (SoundDesk 11)</li>
      <li>Sound Design</li>
      <li>Sound Acoustics</li>
      <li>Studio Recording</li>
      <li>Audio Editing</li>
      <li>Audio Mixing</li>
      <li>Analog/Digital<br>board operation</li>
      <li>Music Arranging</li>
      <li>Music Composition</li>
      <li>Music Production</li>
      <li>Composing Sheet Music</li>
      <li>Singer-songwriter</li>
      <li>Rhythm guitarist</li>
    </ul>
  </main>
</body>
</html>
```